ATM Website-Great Opportunity for Portability

Hey We need YOU to help us make our ATM (Automatic Teller Machine)Website!!) We are a million dollar business that will look great on your portfolio! Our Name is "CORNER CASH POINT"
Previous ATM business (now sold) was www.cashbrivo.com.au (site being pulled down so look at it fast!)
The winner will get the same package that we will giving to the winner of our other project! (worth over $9,000)
http://jobs.pixelvorn.com/job.aspx?id=4827
**we are making a series of sites/applications Winners will be solo invited to work on all upcoming projects of that catigory**
***we are also looking for Outstanding freelance guys to work with on all future projects***
Main Points!!
1: one main page (that is not a blog!)
2: Then the Theme!
3: I don't want it to look like a word-press
I.e like this guys Word press http://www.trasqueld.com/
See how he has one main page then the rest are WP Theme :)
Key points to the Home Page!
See attached pic for the menu's needed and the call now key.
Main page needs to have
1. Clean, uncluttered, and follow the feel of our LOGO (attached) Be creative but simplistic with the page. Round curves are good)
2. Large hero images of happy poeple in the community but not looking too stocky or contrived - natural smiles, natural expressions, With Image of OUR ATM on the page!
3. Easy navigation
4: (3 big buttons like on our competitors site
(http://www.brightfundpoint.com.au/) With the titles
(get an ATM (and beside it "for your business")
(Own an ATM (increase your investment Portfolio)
(Latest ATM (See an ATM in action)
For the Theme Page,
It must flow on from the main menu but have a bread crum trail on the page of all the sub links somewhere on the left of the page (or somewhere else that might look better.
Theme page should have a Call now or email now option!! If you can fit in 2 without it looking cluttered that would be good.
I will attach our brochures so you can get a feel of our product.
Also you should be able to extract images from our brochure using GLEMBRA DOC TOOL or similar PDF editor if needed!!
logo attached and also found at www.cornercashpoint.com.au
Good Fonts to use!
Helvetica Neue LT (bold thin ect)
Helvetica Neue LT Com
Target Market(s)
Business Owners and Investors
Industry/Entity Type
Investment
Requirements
Must have
- The Call now Features in the attached file, Clean layout
Should not have
- Should not look like stock photo's and a cheap website or a template...

```html
<!DOCTYPE html>
<html lang="en">
<head>
<meta charset="utf-8">
<title>Corner Cash Point – Home</title>
<link rel="stylesheet" href="https://fonts.googleapis.com/css2?family=Arimo:wght@400;700&family=Roboto+Condensed:wght@400;700&display=swap">
<style>
  :root {
    --brand-green: #8cc63f;
    --deep-green: #1f6e12;
    --mid-green: #4e9a3a;
    --soft-green: #9bc98a;
    --alert-red: #ef2b2d;
    --ink: #222;
    --nav-top: #c9cacc;
    --nav-bottom: #a3a4a7;
    --panel-shadow: rgba(0,0,0,.25);
    --logo-grey: #9a9a9a;
  }
  * { box-sizing: border-box; margin: 0; padding: 0; }
  html, body { width: 1200px; height: 857px; overflow: hidden; }
  body { background: #fff; font-family: "Arimo", Arial, sans-serif; color: var(--ink); position: relative; }

  .site-header { position: absolute; left: 0; top: 0; width: 1200px; height: 131px; }
  .brand { position: absolute; left: 169px; top: 30px; display: flex; align-items: center; gap: 8px; }
  .brand-dot { width: 56px; height: 56px; border-radius: 50%; background: var(--brand-green); }
  .brand-name { font-family: "Roboto Condensed", sans-serif; font-weight: 700; font-size: 17px; color: var(--logo-grey); line-height: 1.1; width: 70px; }

  .share { position: absolute; left: 915px; top: 10px; width: 136px; height: 28px; border-bottom: 1px solid #222; display: flex; align-items: center; gap: 8px; padding-left: 10px; }
  .share-label { font-size: 12px; font-weight: 700; }
  .share-btn { width: 20px; height: 20px; border-radius: 3px; }
  .share-btn.one { background: #3b5a9a; }
  .share-btn.two { background: #55b9e8; }

  .helpline-photo { position: absolute; left: 741px; top: 33px; width: 61px; height: 98px; background: linear-gradient(180deg, #e9d3b0 0%, #e04040 45%, #2a2a2a 100%); border-radius: 4px 4px 0 0; }
  .helpline { position: absolute; left: 818px; top: 79px; font-family: "Roboto Condensed", sans-serif; }
  .helpline-q { font-size: 18px; color: #333; }
  .helpline-call { font-size: 24px; color: var(--alert-red); margin-top: 2px; }
  .helpline-call b { font-weight: 700; }

  .main-nav { position: absolute; left: 150px; top: 131px; width: 900px; height: 38px; border-radius: 4px; background: linear-gradient(var(--nav-top), var(--nav-bottom)); display: flex; padding-left: 18px; gap: 24px; }
  .main-nav a { font-size: 13.5px; color: #222; text-decoration: none; line-height: 36px; position: relative; }
  .main-nav a.current::after { content: ""; position: absolute; left: 0; right: 0; bottom: -2px; height: 3px; background: var(--brand-green); }

  .content-panel { position: absolute; left: 150px; top: 197px; width: 900px; height: 544px; background: #fff; border-radius: 4px; box-shadow: 0 1px 5px var(--panel-shadow); }

  .hero { position: absolute; left: 0; top: 19px; width: 900px; height: 281px; background: radial-gradient(ellipse at 55% 100%, #0f5e0a 0%, var(--mid-green) 55%, var(--soft-green) 100%); }
  .hero-photo { position: absolute; left: 33px; top: 18px; width: 258px; height: 272px; border-radius: 6px; background: linear-gradient(90deg, #4a9a3a 0%, #8fbf6a 50%, #e8e4dc 75%, #1f1f2a 100%); }
  .hero-copy { position: absolute; left: 309px; top: 43px; width: 290px; color: #fff; }
  .hero-title { font-family: "Roboto Condensed", sans-serif; font-size: 21px; font-weight: 400; white-space: nowrap; text-shadow: 0 1px 2px rgba(0,0,0,.35); }
  .hero-text { font-size: 11.5px; line-height: 22.5px; margin-top: 14px; width: 282px; }
  .hero-call { font-size: 17px; margin-top: 17px; }
  .hero-call b { color: var(--alert-red); font-weight: 700; }

  .enquiry { position: absolute; left: 609px; top: 28px; width: 282px; height: 225px; border-radius: 4px; background: linear-gradient(#fff, #e3e3e3); overflow: hidden; box-shadow: 0 1px 3px rgba(0,0,0,.3); }
  .enquiry-corner { position: absolute; }
  .enquiry-title { position: absolute; left: 18px; top: 12px; font-family: "Roboto Condensed", sans-serif; font-size: 17px; color: var(--deep-green); display: flex; align-items: center; gap: 18px; }
  .enquiry-title::after { content: ""; width: 85px; height: 2px; background: var(--deep-green); }
  .enquiry-text { position: absolute; left: 18px; top: 40px; width: 230px; font-size: 11.5px; line-height: 17px; color: #222; }
  .field { position: absolute; left: 47px; width: 188px; height: 19px; border: 1px solid var(--deep-green); background: #fff; font-size: 11px; color: #888; padding-left: 8px; line-height: 17px; }
  .send-btn { position: absolute; left: 113px; top: 167px; width: 150px; height: 28px; border-radius: 3px; background: linear-gradient(#58a845, #1d6a12); color: #fff; font-size: 16px; text-align: center; line-height: 28px; }

  .feature-tiles { position: absolute; left: 9px; top: 328px; display: flex; gap: 18px; }
  .tile { position: relative; width: 282px; height: 188px; border-radius: 4px; overflow: hidden; }
  .tile.business { background: linear-gradient(135deg, #3f6e8a, #a9b6bd 55%, #6a7f8c); }
  .tile.investment { background: linear-gradient(180deg, #8a6a4a, #5d5a5a 50%, #2f2a2a); }
  .tile.action { background: linear-gradient(135deg, #b58a54, #d7b187 45%, #3a3024); }
  .tile-title { position: absolute; left: 18px; top: 14px; font-family: "Roboto Condensed", sans-serif; font-size: 22px; color: #fff; text-shadow: 0 1px 3px rgba(0,0,0,.6); }
  .tile-caption { position: absolute; left: 0; right: 0; bottom: 0; height: 38px; background: rgba(0,0,0,.45); color: #fff; font-family: "Roboto Condensed", sans-serif; font-size: 16px; text-align: right; padding-right: 18px; line-height: 38px; }

  .site-footer { position: absolute; left: 169px; top: 765px; }
  .footer-nav { font-size: 11.5px; color: #222; }
  .footer-nav a { color: inherit; text-decoration: none; }
  .footer-nav a.highlight { color: var(--brand-green); }
  .footer-nav .sep { margin: 0 5px; }
  .copyright { font-size: 10.5px; margin-top: 10px; }
  .copyright span { color: var(--brand-green); }

  .footer-brand { position: absolute; left: 945px; top: 765px; display: flex; align-items: center; gap: 6px; }
  .footer-brand .brand-dot { width: 36px; height: 36px; background: var(--logo-grey); }
  .footer-brand .brand-name { font-size: 12px; width: 56px; }
</style>
</head>
<body>
  <header class="site-header">
    <div class="brand">
      <span class="brand-dot"></span>
      <span class="brand-name">CORNER CASH POINT</span>
    </div>
    <div class="share">
      <span class="share-label">Share Us:</span>
      <span class="share-btn one" aria-label="Share on social network"></span>
      <span class="share-btn two" aria-label="Share on social network"></span>
    </div>
    <div class="helpline-photo" role="img" aria-label="Smiling woman holding a red telephone handset"></div>
    <div class="helpline">
      <div class="helpline-q">Need Help?</div>
      <div class="helpline-call">Call on: <b>1300 482 117</b></div>
    </div>
  </header>

  <nav class="main-nav">
    <a class="current" href="#">Home</a>
    <a href="#">About</a>
    <a href="#">Investors</a>
    <a href="#">Products &amp; Services</a>
    <a href="#">Get a Free ATM</a>
    <a href="#">Giving Back</a>
    <a href="#">Who has One</a>
    <a href="#">Media</a>
    <a href="#">Career</a>
  </nav>

  <main class="content-panel">
    <section class="hero">
      <div class="hero-photo" role="img" aria-label="Green branded ATM with a smiling woman using it"></div>
      <div class="hero-copy">
        <h1 class="hero-title">Welcome to CORNER CASH POINT</h1>
        <p class="hero-text">Lorem Ipsum is simply dummy text of the printing and typesetting industry. Lorem Ipsum has been the industry's standard dummy text ever since the 1500s, when an unknown printer took a galley of type and scrambled it to make a type specimen book.</p>
        <p class="hero-call">Call Us on: <b>1300 482 117</b></p>
      </div>

      <form class="enquiry">
        <svg class="enquiry-corner" style="left:197px;top:0" width="85" height="85"><polygon points="0,0 85,0 85,85" fill="#8cc63f"/></svg>
        <svg class="enquiry-corner" style="left:0;top:140px" width="90" height="85"><polygon points="0,0 0,85 90,85" fill="#8cc63f"/></svg>
        <div class="enquiry-title">Get in Thouch</div>
        <p class="enquiry-text">Lorem Ipsum is simply dummy text of the printing and typesetting industry.</p>
        <div class="field" style="top:79px">Name</div>
        <div class="field" style="top:107px">Email Id</div>
        <div class="field" style="top:135px">Phone</div>
        <div class="send-btn">Get In Thouch</div>
      </form>
    </section>

    <section class="feature-tiles">
      <a class="tile business" role="img" aria-label="Hand holding out a bank card">
        <span class="tile-title">Get an ATM</span>
        <span class="tile-caption">For your Business</span>
      </a>
      <a class="tile investment" role="img" aria-label="People queuing at a row of ATMs">
        <span class="tile-title">Own an ATM</span>
        <span class="tile-caption">Increase your investment Portfolio</span>
      </a>
      <a class="tile action" role="img" aria-label="Hand taking cash from an ATM">
        <span class="tile-title">Latest ATM</span>
        <span class="tile-caption">See an ATM in action</span>
      </a>
    </section>
  </main>

  <footer class="site-footer">
    <nav class="footer-nav">
      <a href="#">Home</a><span class="sep">|</span><a href="#">About</a><span class="sep">|</span><a href="#">Investors</a><span class="sep">|</span><a href="#">Products &amp; Services</a><span class="sep">|</span><a class="highlight" href="#">Get a Free ATM</a><span class="sep">|</span><a href="#">Giving Back</a><span class="sep">|</span><a href="#">Who has One</a><span class="sep">|</span><a href="#">Media</a><span class="sep">|</span><a href="#">Career</a>
    </nav>
    <p class="copyright">© 2010 <span>Corner Cash Point</span>. All Rights Reserved.</p>
  </footer>
  <div class="footer-brand">
    <span class="brand-dot"></span>
    <span class="brand-name">CORNER CASH POINT</span>
  </div>
</body>
</html>
```